New Business Card Design Project

Hi! I would like for you to design a business card for our aesthetic injections business. We offer Velmo, filler, skin care. I would like it to be elegant, feminine, modern and sleek/clean. I like black/gold foil/ivory/parchment colors. It can be either one or two sided. I would like matte black with gold foil logo on one side and ivory with gold foil information on the other side

Target Market(s)

target market is the discerning woman who wants to look her best

Industry/Entity Type

beauty

Contact Information for Business Card

logo, name, phone, email, website, instagram, facebook, location

Requirements
Must have
• logo and info
Nice to have
• the icons for cell, instagram, email, fb etc
Should not have
• images of people

```html
<!DOCTYPE html>
<html lang="en">
<head>
<meta charset="utf-8">
<title>The Velvet Studio — Business Card</title>
<link rel="stylesheet" href="https://fonts.googleapis.com/css2?family=Poppins:wght@400&family=Mrs+Saint+Delafield&display=swap">
<style>
  :root {
    --backdrop: #d9d7d5;
    --matte-black: #222223;
    --ivory: #f4f1e4;
    --pattern-tone: #efe9d2;
    --gold: #b4893b;
    --gold-light: #d4b06a;
    --ink: #1b1b1b;
  }
  html, body {
    margin: 0;
    padding: 0;
    width: 1200px;
    height: 1200px;
    overflow: hidden;
    background: var(--backdrop);
  }
  .canvas {
    position: relative;
    width: 1200px;
    height: 1200px;
  }
  .card {
    position: absolute;
    left: 242px;
    width: 703px;
    height: 400px;
    overflow: hidden;
  }
  .card--front {
    top: 170px;
    background: var(--matte-black);
  }
  .card--back {
    top: 629px;
    background: var(--ivory);
  }

  /* Brand mark: name inside a plain circle */
  .brand {
    position: absolute;
    border-radius: 50%;
    display: flex;
    align-items: center;
    justify-content: center;
    text-align: center;
    font-family: "Poppins", sans-serif;
    font-weight: 400;
    text-transform: uppercase;
    box-sizing: border-box;
  }
  .brand--front {
    left: 248px;
    top: 96px;
    width: 208px;
    height: 208px;
    border: 1.5px solid var(--gold);
    color: var(--gold-light);
    font-size: 17px;
    letter-spacing: 5px;
    line-height: 1.7;
  }
  .brand--back {
    left: 110px;
    top: 83px;
    width: 140px;
    height: 140px;
    border: 1.2px solid var(--ink);
    color: var(--ink);
    font-size: 11.5px;
    letter-spacing: 3.5px;
    line-height: 1.7;
  }

  .pattern-panel {
    position: absolute;
    left: 0;
    top: 0;
    width: 330px;
    height: 400px;
    background: linear-gradient(160deg, var(--pattern-tone), var(--ivory));
  }

  .social {
    position: absolute;
    left: 0;
    width: 356px;
    top: 270px;
    display: flex;
    justify-content: center;
    align-items: center;
    gap: 6px;
    font-family: "Poppins", sans-serif;
    font-size: 12px;
    letter-spacing: 1px;
    color: var(--ink);
  }
  .social__dot {
    width: 12px;
    height: 12px;
    border-radius: 50%;
    background: var(--ink);
  }
  .website {
    position: absolute;
    left: 0;
    width: 356px;
    top: 296px;
    text-align: center;
    font-family: "Poppins", sans-serif;
    font-size: 13px;
    letter-spacing: 1px;
    color: var(--ink);
  }

  .holder-name {
    position: absolute;
    left: 354px;
    top: 42px;
    font-family: "Mrs Saint Delafield", cursive;
    font-size: 50px;
    color: var(--gold);
    line-height: 1;
  }

  .info {
    position: absolute;
    left: 354px;
    font-family: "Poppins", sans-serif;
    font-size: 15px;
    letter-spacing: 3px;
    color: var(--gold);
    text-transform: uppercase;
    line-height: 20px;
  }
  .info--address { top: 198px; }
  .info-row {
    position: absolute;
    left: 364px;
    display: flex;
    align-items: center;
    gap: 8px;
    font-family: "Poppins", sans-serif;
    font-size: 15px;
    letter-spacing: 2.6px;
    color: var(--gold);
    text-transform: uppercase;
  }
  .info-row--phone { top: 266px; }
  .info-row--email { top: 294px; }
  .info-icon { width: 18px; height: 18px; flex: none; }
  .pin-icon {
    position: absolute;
    left: 354px;
    top: 160px;
  }
</style>
</head>
<body>
<main class="canvas">

  <section class="card card--front" aria-label="Card front">
    <div class="brand brand--front">The<br>Velvet<br>Studio</div>
  </section>

  <section class="card card--back" aria-label="Card back">
    <div class="pattern-panel" role="img" aria-label="Faint ivory floral pattern"></div>

    <div class="brand brand--back">The<br>Velvet<br>Studio</div>

    <div class="social"><span class="social__dot"></span>@velvetstudio</div>
    <div class="website">WWW.VELVETSTUDIO.COM</div>

    <div class="holder-name">Clara Vance</div>

    <svg class="pin-icon" width="22" height="30" viewBox="0 0 22 30" aria-hidden="true">
      <path d="M11 1C5.8 1 2 4.9 2 9.8 2 16 11 24 11 24s9-8 9-14.2C20 4.9 16.2 1 11 1z" fill="var(--gold)"/>
      <circle cx="11" cy="9.8" r="3.3" fill="var(--ivory)"/>
      <rect x="2" y="27" width="18" height="2" fill="var(--gold)"/>
    </svg>
    <div class="info info--address">PO.Box, State<br>Country</div>

    <div class="info-row info-row--phone">
      <svg class="info-icon" viewBox="0 0 24 24" aria-hidden="true">
        <path d="M6.6 10.8c1.4 2.8 3.8 5.1 6.6 6.6l2.2-2.2c.3-.3.7-.4 1-.2 1.1.4 2.3.6 3.6.6.6 0 1 .4 1 1V20c0 .6-.4 1-1 1C10.6 21 3 13.4 3 4c0-.6.4-1 1-1h3.5c.6 0 1 .4 1 1 0 1.3.2 2.5.6 3.6.1.3 0 .7-.2 1l-2.3 2.2z" fill="var(--gold)"/>
      </svg>
      (555) 201 4837
    </div>
    <div class="info-row info-row--email">
      <svg class="info-icon" viewBox="0 0 24 24" aria-hidden="true">
        <rect x="2" y="5" width="20" height="14" fill="var(--gold)"/>
        <path d="M2 5l10 8 10-8" fill="none" stroke="var(--ivory)" stroke-width="1.6"/>
      </svg>
      hello@velvetstudio.com
    </div>
  </section>

</main>
</body>
</html>
```